Commercial Construction Company

We need a business card design based on our current logo. We are a commercial general contractor based in Southern California that specializes in bank remodels. We would like to see designs that incorporate dark blue. The final design should portray an image of professionalism and quality.

If possible, I would like to add metallic foil to the design. Thank you

```html
<!DOCTYPE html>
<html lang="en">
<head>
<meta charset="utf-8">
<title>Merrow Commercial Construction Services – Business Card</title>
<link rel="stylesheet" href="https://fonts.googleapis.com/css2?family=Open+Sans:wght@400;600&display=swap">
<style>
  :root {
    --navy: #00123a;
    --slate: #9a9ea4;
    --white: #ffffff;
    --ink: #0a0a0a;
    --backdrop: #d9d9d9;
    --foil-dark: #8d8f93;
    --foil-light: #f7f7f7;
  }
  * { box-sizing: border-box; margin: 0; padding: 0; }
  html, body {
    width: 1200px; height: 1200px; overflow: hidden;
    background: var(--backdrop);
    font-family: "Open Sans", Arial, sans-serif;
  }
  .canvas { position: relative; width: 1200px; height: 1200px; }
  .card {
    position: absolute; left: 250px; width: 700px; height: 400px;
    box-shadow: 0 14px 30px rgba(0,0,0,0.25);
    overflow: hidden;
  }
  .card--front { top: 150px; background: var(--navy); }
  .card--back { top: 640px; background: var(--white); display: flex; }

  .brand {
    position: absolute; inset: 0;
    display: flex; align-items: center; justify-content: center;
    padding: 0 40px;
  }
  .brand__name {
    font-weight: 600; color: var(--white);
    font-size: 30px; line-height: 1.25; text-align: center;
  }

  .contact {
    position: relative; width: 420px; height: 100%;
    background: var(--navy); padding: 58px 44px 0 44px;
  }
  .foil {
    width: 14px; height: 100%;
    background: linear-gradient(180deg, var(--foil-dark) 0%, var(--foil-light) 50%, var(--foil-dark) 100%);
  }
  .contact__name {
    font-size: 34px; font-weight: 600; color: var(--slate); letter-spacing: 0.5px; line-height: 1;
  }
  .contact__role {
    font-size: 18px; color: var(--slate); margin-top: 4px; letter-spacing: 0.5px;
  }
  .contact__rule {
    border: 0; border-top: 1.5px solid var(--slate); margin: 14px 0 24px; width: 330px;
  }
  .contact__list { list-style: none; }
  .contact__item {
    display: flex; align-items: flex-start; gap: 16px;
    font-size: 19px; color: var(--slate); margin-bottom: 13px; line-height: 1.25;
  }
  .contact__item svg { width: 20px; height: 20px; flex: none; margin-top: 3px; fill: var(--slate); }

  .card__face { flex: 1; position: relative; background: var(--white); }
  .card__face .brand { padding: 0 28px; }
  .card__face .brand__name { color: var(--ink); font-size: 20px; }
</style>
</head>
<body>
<main class="canvas">
  <section class="card card--front">
    <div class="brand">
      <p class="brand__name">Merrow Commercial<br>Construction Services</p>
    </div>
  </section>

  <section class="card card--back">
    <div class="contact">
      <h1 class="contact__name">JOHN SMITH</h1>
      <p class="contact__role">MANAGER</p>
      <hr class="contact__rule">
      <ul class="contact__list">
        <li class="contact__item">
          <svg viewBox="0 0 24 24"><path d="M2 5h20v14H2V5zm2 2v.5l8 5 8-5V7H4z"/></svg>
          <span>yourname@email.com</span>
        </li>
        <li class="contact__item">
          <svg viewBox="0 0 24 24"><path d="M6.6 10.8a15 15 0 006.6 6.6l2.2-2.2c.3-.3.7-.4 1-.2 1.1.4 2.3.6 3.6.6.6 0 1 .4 1 1V20c0 .6-.4 1-1 1A17 17 0 013 4c0-.6.4-1 1-1h3.5c.6 0 1 .4 1 1 0 1.3.2 2.5.6 3.6.1.3 0 .7-.2 1l-2.3 2.2z"/></svg>
          <span>(00) 1234-5678</span>
        </li>
        <li class="contact__item">
          <svg viewBox="0 0 24 24"><path d="M7 2h10a1 1 0 011 1v18a1 1 0 01-1 1H7a1 1 0 01-1-1V3a1 1 0 011-1zm1 2v14h8V4H8zm4 15.2a.9.9 0 100 1.8.9.9 0 000-1.8z"/></svg>
          <span>+01 234 567 8910</span>
        </li>
        <li class="contact__item">
          <svg viewBox="0 0 24 24"><path d="M12 2a7 7 0 00-7 7c0 5 7 13 7 13s7-8 7-13a7 7 0 00-7-7zm0 9.5A2.5 2.5 0 1112 6.5a2.5 2.5 0 010 5z"/></svg>
          <span>Your address line 1,<br>Your address line 2</span>
        </li>
      </ul>
    </div>
    <div class="foil"></div>
    <div class="card__face">
      <div class="brand">
        <p class="brand__name">Merrow Commercial<br>Construction Services</p>
      </div>
    </div>
  </section>
</main>
</body>
</html>
```